a4 size poster for theatre school

I am looking for an eye catching poster for my theatre school - Bright Lantern Stage school - View our website here for the style we have already www.brightlanternstage.co.uk

Wording needs to include;

* Award Winning, Accredited, Affordable Performing Arts Classes taught by Leading Industry Experts

* Ages 4- 21 years

* All classes contain all three disciplines of Drama, Singing & Dance keeping cost low and enjoyment high

* Classes offered;
Drama
QWERN
Singing
PBSO dance
Freestyle Ballet
Freestyle Tap
Contemporary
Street
Jazz Musical Theatre

* FREE casting agency for TV and Theatre Available. Ten pupils currently performing in West End Productions, 8 pupils currently on screen in TV commercials, several pupils currently working on film & TV projects for Zentrovia, Velmora Plus & Kestrel TV.

* Optional PBSO and QWERN exams

* Unparalleled performance opportunities both locally and in the West End

Our quality training is evident in our pupils success

* Now in our successful 17th Year!

* Awarded recognition from the Board for Youth Stagecraft and Movement Studies - The industry regulator for children's performing arts training.

Target Market(s)

Parents & Children ages 4-21 years

Industry/Entity Type

Performing arts

Font styles to use
Other font styles liked:
• Arvo

Colors
EB3D1F
EC4F4E
F09395
F8D3D4
FCEDEE
6B429C
8869AF
B7A5CE
E3DAEB
F3F0F8

Requirements
Must have
• A good mix of photo's pf boys & girls. Different ethnicities. Different ages
Nice to have
• Wording very clear
Should not have
• Too many words

```html
<!DOCTYPE html>
<html lang="en">
<head>
<meta charset="utf-8">
<title>Bright Lantern Stage school poster</title>
<link href="https://fonts.googleapis.com/css2?family=Roboto+Slab:wght@400;500;700&family=Arvo:wght@400;700&family=Roboto+Condensed:wght@700&display=block" rel="stylesheet">
<style>
:root{
  --backdrop:#333333;
  --navy:#0e0b33;
  --red:#e8401f;
  --yellow:#e9e05a;
  --white:#ffffff;
  --ink:#1a1a1a;
  --teal:#27a3c4;
  --tick-grey:#9a9a9a;
  --slab:"Roboto Slab","Arvo","Rockwell","Roboto Slab Fallback",serif;
}
*{box-sizing:border-box;margin:0;padding:0}
html,body{width:961px;height:1200px;overflow:hidden;background:var(--backdrop)}
body{position:relative;font-family:var(--slab);color:var(--ink)}
.poster{position:absolute;left:157px;top:142px;width:1000px;height:1415px;transform:scale(.6476);transform-origin:0 0;background:var(--white);overflow:hidden;font-family:var(--slab)}
.abs{position:absolute}
.hero-photo{left:0;top:0;width:1000px;height:630px;background:radial-gradient(ellipse at 55% 40%,#6a2f8c 0%,#35349e 35%,#1c1d6b 70%,#0e0b33 100%)}
.hero-band{left:0;top:630px;width:1000px;height:140px;background:var(--navy)}
.hero-fade{left:0;top:520px;width:1000px;height:110px;background:linear-gradient(rgba(14,11,51,0),var(--navy))}
.year-line{left:0;top:40px;width:1000px;text-align:center;color:var(--white);font-weight:700;font-size:28px;letter-spacing:7px;white-space:nowrap}
.school-name{left:700px;top:150px;width:290px;display:flex;align-items:center;gap:12px;color:var(--red);font-weight:700;font-size:34px;line-height:1.1}
.school-name .dot{flex:none;width:26px;height:26px;border-radius:50%;background:var(--yellow)}
.age-badge{left:105px;top:188px;width:175px;height:175px;border-radius:50%;background:var(--red);color:var(--white);font-weight:700;font-size:38px;line-height:36px;text-align:center;display:flex;align-items:center;justify-content:center}
.claims{left:93px;top:478px;color:var(--white);font-weight:700;font-size:66px;line-height:68px;white-space:nowrap;text-shadow:0 2px 6px rgba(0,0,0,.4)}
.claim{display:inline-flex;align-items:center;gap:12px;margin-right:14px}
.tick-box{width:48px;height:48px;background:var(--yellow);border-radius:4px;display:inline-block}
.tagline{left:93px;top:640px;color:var(--white);font-size:48px;line-height:46px;white-space:nowrap}
.tagline strong{color:var(--yellow);font-weight:700}
.diagonal{left:0;top:745px}
.classes-photo{left:520px;top:772px;width:480px;height:303px;background:linear-gradient(160deg,#c9621f 0%,#d9462c 50%,#8a2a4a 100%)}
.classes-box{left:20px;top:818px;width:686px;height:148px;border:5px solid var(--red);background:rgba(255,255,255,.82)}
.classes-title{left:232px;top:802px;padding:0 12px;background:var(--white);font-weight:700;font-size:26px;line-height:30px;color:var(--ink)}
.class-list{left:45px;top:842px;display:grid;grid-template-columns:138px 234px 270px;row-gap:8px;font-size:24px;white-space:nowrap}
.class-item{display:flex;align-items:center;gap:10px;height:28px}
.class-item svg{flex:none}
.grid-photo{width:233px;height:156px}
.p1{left:19px;top:992px;background:linear-gradient(135deg,#e9b526,#d9853a)}
.p2{left:267px;top:992px;background:linear-gradient(135deg,#c9c9e6,#6b5a4a)}
.p3{left:19px;top:1163px;background:linear-gradient(135deg,#1a1d5a,#3b3f8e)}
.p4{left:267px;top:1163px;background:linear-gradient(135deg,#6a1c1c,#b23a32)}
.casting{left:550px;top:1103px;width:440px}
.casting h2{color:var(--red);font-weight:700;font-size:30px;line-height:34px;white-space:nowrap}
.casting ul{list-style:none;margin-top:2px;font-size:20px;line-height:27.5px}
.casting li::before{content:"» ";color:var(--tick-grey)}
.footer-red{left:270px;top:1336px;width:730px;height:79px;background:var(--red)}
.footer-note{left:345px;top:1348px;width:330px;color:var(--white);font-size:13px;line-height:16px}
.exam-box{left:697px;top:1318px;width:251px;height:97px;background:var(--yellow);display:flex;align-items:center;justify-content:center;text-align:center;font-weight:700;font-size:26px;line-height:27px;color:var(--ink)}
.scheme{left:3px;top:1336px;width:262px;height:48px;background:var(--teal);display:flex;align-items:center;gap:10px;padding-left:12px;color:var(--white);font-weight:700;font-size:30px}
.scheme .sq{width:22px;height:22px;background:var(--white)}
.scheme-caption{left:14px;top:1398px;font-family:"Roboto Condensed","Arial Narrow",sans-serif;font-weight:700;font-size:12px;color:var(--ink)}
.scheme-caption span{color:var(--teal)}
</style>
</head>
<body>
<div class="poster">
  <div class="abs hero-photo" role="img" aria-label="Stage photo of three young dancers leaping under blue and purple spotlights"></div>
  <div class="abs hero-band"></div>
  <div class="abs hero-fade"></div>

  <p class="abs year-line">NOW IN OUR SUCCESSFUL 17TH YEAR!</p>
  <div class="abs school-name"><span class="dot"></span><span>Bright Lantern Stage school</span></div>
  <div class="abs age-badge">Ages<br>4-21<br>years</div>

  <div class="abs claims">
    <div><span class="claim"><span class="tick-box"><svg width="48" height="48" viewBox="0 0 48 48"><path d="M12 25l8 8 16-17" fill="none" stroke="#111" stroke-width="6" stroke-linecap="round" stroke-linejoin="round"/></svg></span>Award Winning</span></div>
    <div><span class="claim"><span class="tick-box"><svg width="48" height="48" viewBox="0 0 48 48"><path d="M12 25l8 8 16-17" fill="none" stroke="#111" stroke-width="6" stroke-linecap="round" stroke-linejoin="round"/></svg></span>Accredited</span><span class="claim"><span class="tick-box"><svg width="48" height="48" viewBox="0 0 48 48"><path d="M12 25l8 8 16-17" fill="none" stroke="#111" stroke-width="6" stroke-linecap="round" stroke-linejoin="round"/></svg></span>Affordable</span></div>
  </div>

  <p class="abs tagline">Performing Arts Classes Taught<br>By <strong>Leading Industry Experts</strong></p>

  <svg class="abs diagonal" width="1000" height="50" viewBox="0 0 1000 50">
    <polygon points="0,5 1000,30 1000,27 520,27 0,45" fill="#e8401f"/>
  </svg>

  <div class="abs classes-photo" role="img" aria-label="Large group of costumed pupils performing on stage in warm orange light"></div>
  <div class="abs classes-box"></div>
  <h2 class="abs classes-title">CLASSES OFFERED</h2>
  <div class="abs class-list">
    <div class="class-item"><svg width="20" height="20" viewBox="0 0 20 20"><rect x="1" y="1" width="18" height="18" fill="none" stroke="#9a9a9a" stroke-width="1.5"/><path d="M5 10l3.5 3.5L15 6" fill="none" stroke="#9a9a9a" stroke-width="1.6"/></svg>Drama</div>
    <div class="class-item"><svg width="20" height="20" viewBox="0 0 20 20"><rect x="1" y="1" width="18" height="18" fill="none" stroke="#9a9a9a" stroke-width="1.5"/><path d="M5 10l3.5 3.5L15 6" fill="none" stroke="#9a9a9a" stroke-width="1.6"/></svg>PBSO dance</div>
    <div class="class-item"><svg width="20" height="20" viewBox="0 0 20 20"><rect x="1" y="1" width="18" height="18" fill="none" stroke="#9a9a9a" stroke-width="1.5"/><path d="M5 10l3.5 3.5L15 6" fill="none" stroke="#9a9a9a" stroke-width="1.6"/></svg>Contemporary</div>
    <div class="class-item"><svg width="20" height="20" viewBox="0 0 20 20"><rect x="1" y="1" width="18" height="18" fill="none" stroke="#9a9a9a" stroke-width="1.5"/><path d="M5 10l3.5 3.5L15 6" fill="none" stroke="#9a9a9a" stroke-width="1.6"/></svg>QWERN</div>
    <div class="class-item"><svg width="20" height="20" viewBox="0 0 20 20"><rect x="1" y="1" width="18" height="18" fill="none" stroke="#9a9a9a" stroke-width="1.5"/><path d="M5 10l3.5 3.5L15 6" fill="none" stroke="#9a9a9a" stroke-width="1.6"/></svg>Freestyle Ballet</div>
    <div class="class-item"><svg width="20" height="20" viewBox="0 0 20 20"><rect x="1" y="1" width="18" height="18" fill="none" stroke="#9a9a9a" stroke-width="1.5"/><path d="M5 10l3.5 3.5L15 6" fill="none" stroke="#9a9a9a" stroke-width="1.6"/></svg>Street</div>
    <div class="class-item"><svg width="20" height="20" viewBox="0 0 20 20"><rect x="1" y="1" width="18" height="18" fill="none" stroke="#9a9a9a" stroke-width="1.5"/><path d="M5 10l3.5 3.5L15 6" fill="none" stroke="#9a9a9a" stroke-width="1.6"/></svg>Singing</div>
    <div class="class-item"><svg width="20" height="20" viewBox="0 0 20 20"><rect x="1" y="1" width="18" height="18" fill="none" stroke="#9a9a9a" stroke-width="1.5"/><path d="M5 10l3.5 3.5L15 6" fill="none" stroke="#9a9a9a" stroke-width="1.6"/></svg>Freestyle Tap</div>
    <div class="class-item"><svg width="20" height="20" viewBox="0 0 20 20"><rect x="1" y="1" width="18" height="18" fill="none" stroke="#9a9a9a" stroke-width="1.5"/><path d="M5 10l3.5 3.5L15 6" fill="none" stroke="#9a9a9a" stroke-width="1.6"/></svg>Jazz Musical Theatre</div>
  </div>

  <div class="abs grid-photo p1" role="img" aria-label="Young children in fairy costumes on a yellow-lit stage"></div>
  <div class="abs grid-photo p2" role="img" aria-label="Children in period costumes acting a scene"></div>
  <div class="abs grid-photo p3" role="img" aria-label="Street dance group performing under blue stage lights"></div>
  <div class="abs grid-photo p4" role="img" aria-label="Young performer singing in front of a costumed chorus"></div>

  <div class="abs casting">
    <h2>FREE casting agency for TV<br>and Theatre Available.</h2>
    <ul>
      <li>10 pupils in West End Productions</li>
      <li>8 pupils in TV commercials</li>
      <li>Several working on film &amp; TV projects for Zentrovia, Velmora Plus &amp; Kestrel TV.</li>
    </ul>
  </div>

  <div class="abs footer-red"></div>
  <p class="abs footer-note">Awarded recognition from the Board for Youth Stagecraft and Movement Studies - The industry regulator for children's performing arts training.</p>
  <div class="abs exam-box">Optional PBSO &amp;<br>QWERN exams</div>
  <div class="abs scheme"><span class="sq"></span>BYSMS</div>
  <p class="abs scheme-caption"><span>Recognised Awards Scheme:</span> Recognised School</p>
</div>
</body>
</html>
```